Pemberly Senior Marketing Biz Card
Biz card and Stationary
Bright & Fun-filled
Marlene Pemberly
Independent Agent
Larkmoor Falls, NC
marlenej.pemberly@postvale-mail.com
PemberlyForSeniors.com
please add photo headshot to the front of the card also. see upload.
Also, please only use white and blue for the wording on the card. DO NOT USE RED.
see upload example for content for back of card
Logo- please use
Headshot
card back content

```html
<!DOCTYPE html>
<html lang="en">
<head>
<meta charset="utf-8">
<title>Pemberly Senior Marketing – Business Card</title>
<link href="https://fonts.googleapis.com/css2?family=Marcellus&family=Marcellus+SC&display=swap" rel="stylesheet">
<style>
  :root {
    --page: #ffffff;
    --card-border: #9a9a9a;
    --brand-blue: #1f6fb8;
    --ink-blue: #2a78c0;
    --ink-grey: #555b63;
    --deep-blue: #0a3f86;
    --mid-blue: #1a67b8;
    --light-blue: #3f8fd8;
    --white: #ffffff;
  }
  * { box-sizing: border-box; margin: 0; padding: 0; }
  html, body {
    width: 1200px; height: 710px; overflow: hidden;
    background: var(--page);
    font-family: "Marcellus", "Optima", serif;
  }
  .canvas { position: relative; width: 1200px; height: 710px; }

  .card {
    position: absolute;
    border: 2px solid var(--card-border);
    overflow: hidden;
  }

  /* Front */
  .card-front { left: 300px; top: 19px; width: 600px; height: 336px; background: var(--white); }
  .front-panel { position: absolute; right: 0; top: 0; width: 215px; height: 100%; }
  .headshot {
    position: absolute; left: 430px; top: 12px; width: 98px; height: 106px;
    background: linear-gradient(160deg, #d9d1cb, #8d7f77 60%, #3e3a3a);
    border: 3px solid var(--white);
  }
  .brand { position: absolute; left: 18px; top: 16px; display: flex; align-items: center; gap: 12px; }
  .brand-mark { width: 72px; height: 72px; border-radius: 50%; background: var(--brand-blue); }
  .brand-name {
    font-family: "Marcellus SC", serif; color: var(--brand-blue);
    font-size: 38px; line-height: 1.0; letter-spacing: 0.5px;
  }
  .brand-name span { display: block; font-size: 20px; margin-top: 2px; }
  .agent-name {
    position: absolute; left: 24px; top: 134px;
    font-family: "Marcellus SC", serif; font-weight: 400; font-size: 30px; color: var(--ink-blue);
  }
  .agent-title {
    position: absolute; left: 26px; top: 172px;
    font-family: "Marcellus SC", serif; font-size: 17px; color: var(--ink-grey); letter-spacing: 0.5px;
  }
  .contact {
    position: absolute; left: 26px; top: 240px;
    font-family: "Marcellus SC", serif; font-size: 14px; line-height: 18px; color: var(--ink-grey);
    list-style: none;
  }
  .contact .label { color: var(--ink-blue); }
  .contact .web { color: var(--ink-blue); }

  /* Backs */
  .card-back { top: 360px; width: 571px; height: 336px; }
  .card-back.light { left: 19px; background: var(--white); }
  .card-back.dark {
    left: 610px; border-color: var(--deep-blue);
    background: radial-gradient(ellipse at 75% 45%, var(--light-blue), var(--mid-blue) 45%, var(--deep-blue) 100%);
  }
  .services-heading {
    position: absolute; left: 26px; top: 34px;
    font-family: "Marcellus SC", serif; font-weight: 400; font-size: 17px; letter-spacing: 0.5px;
  }
  .services {
    position: absolute; left: 26px; top: 82px; list-style: none;
    font-family: "Marcellus SC", serif; font-size: 17px; letter-spacing: 0.3px;
  }
  .services li { height: 30px; display: flex; align-items: center; }
  .services li::before { content: "–"; margin-right: 8px; }
  .services li.minor { font-size: 13px; height: 26px; }
  .light .services-heading, .light .services li::before { color: var(--ink-blue); }
  .light .services { color: var(--ink-grey); }
  .dark .services-heading, .dark .services { color: var(--white); }
  .back-mark {
    position: absolute; left: 420px; top: 110px; width: 122px; height: 122px; border-radius: 50%;
  }
  .light .back-mark { background: var(--brand-blue); }
  .dark .back-mark { background: var(--white); }
</style>
</head>
<body>
<main class="canvas">

  <section class="card card-front">
    <svg class="front-panel" viewBox="0 0 215 336" preserveAspectRatio="none" role="img" aria-label="Blue panel with star pattern">
      <defs>
        <linearGradient id="panelFill" x1="0" y1="0" x2="1" y2="1">
          <stop offset="0" stop-color="#3f8fd8"/>
          <stop offset="0.5" stop-color="#1a67b8"/>
          <stop offset="1" stop-color="#0a3f86"/>
        </linearGradient>
      </defs>
      <path d="M25 0 H215 V336 H70 C40 250 10 150 25 0 Z" fill="url(#panelFill)"/>
    </svg>
    <div class="headshot" role="img" aria-label="Headshot photo of Marlene Pemberly"></div>

    <div class="brand">
      <div class="brand-mark"></div>
      <div class="brand-name">Pemberly<span>Senior Marketing</span></div>
    </div>

    <h1 class="agent-name">Marlene Pemberly</h1>
    <p class="agent-title">Independent Agent</p>

    <ul class="contact">
      <li>Larkmoor Falls, NC</li>
      <li><span class="label">Cell:</span> 919-555-0142 | <span class="label">Phone:</span> 919-555-0187</li>
      <li><span class="label">Email:</span> marlenej.pemberly@postvale-mail.com</li>
      <li class="web">www.PemberlyForSeniors.com</li>
    </ul>
  </section>

  <section class="card card-back light">
    <h2 class="services-heading">I can also help you with……</h2>
    <ul class="services">
      <li>Long-Term Care Insurance</li>
      <li class="minor">Fixed Annuities:</li>
      <li>Life Insurance</li>
      <li>Medicare Supplement Insurance</li>
      <li>Individual Major Medical Insurance</li>
      <li>Final Expense Insurance</li>
      <li>Medicare Advantage Plans</li>
    </ul>
    <div class="back-mark"></div>
  </section>

  <section class="card card-back dark">
    <h2 class="services-heading">I can also help you with……</h2>
    <ul class="services">
      <li>Long-Term Care Insurance</li>
      <li class="minor">Fixed Annuities:</li>
      <li>Life Insurance</li>
      <li>Medicare Supplement Insurance</li>
      <li>Individual Major Medical Insurance</li>
      <li>Final Expense Insurance</li>
      <li>Medicare Advantage Plans</li>
    </ul>
    <div class="back-mark"></div>
  </section>

</main>
</body>
</html>
```